Brightvantage.com tech company website

Current site is www.brightvantage.com. The site will tell you about our company.

Designs we like are:
http://megainfo.quellorix.com
www.trelvo.com
www.morvasket.com

Target Market(s)

B2B

Industry/Entity Type

It Company

Coding

Coded - Design and coding required

Number of Pages Required

5+ page

Requirements
Must have
• We want to entice without giving away too much info. We like graphics and colors. But website must look official and credible.

```html
<!DOCTYPE html>
<html lang="en">
<head>
<meta charset="utf-8">
<title>Brightvantage</title>
<link rel="stylesheet" href="https://fonts.googleapis.com/css2?family=Open+Sans:wght@400;600;700;800&display=swap">
<style>
  :root {
    --brand-blue: #1c5f98;
    --brand-navy: #143f68;
    --band-blue: #1f5a8c;
    --band-deep: #174a76;
    --text-dark: #3a3a3a;
    --nav-text: #2b4c6e;
    --footer-bg: #3d3f42;
    --hero-bg: #eef1f4;
    --white: #ffffff;
  }
  * { box-sizing: border-box; margin: 0; padding: 0; }
  html, body { width: 755px; height: 1200px; overflow: hidden; }
  body {
    font-family: "Open Sans", Arial, sans-serif;
    background: var(--white);
    color: var(--text-dark);
    position: relative;
  }

  /* Header */
  .site-header {
    height: 46px;
    display: flex;
    align-items: center;
    justify-content: space-between;
    padding: 0 22px 0 18px;
    border-top: 3px solid var(--brand-blue);
    background: var(--white);
  }
  .brand {
    display: flex;
    align-items: center;
    gap: 7px;
    font-weight: 800;
    font-size: 17px;
    letter-spacing: 0.5px;
    color: var(--brand-blue);
  }
  .brand-dot {
    width: 14px; height: 14px; border-radius: 50%;
    background: var(--brand-blue);
  }
  .main-nav { display: flex; align-items: center; }
  .main-nav a {
    font-size: 8.5px;
    font-weight: 700;
    color: var(--nav-text);
    text-decoration: none;
    padding: 0 10px;
    border-left: 1px solid #b8c3ce;
    line-height: 10px;
  }
  .main-nav a:first-child { border-left: none; }

  /* Hero */
  .hero {
    position: relative;
    height: 318px;
    background: var(--hero-bg);
    overflow: hidden;
  }
  .hero-visual {
    position: absolute;
    right: 0; top: 0;
    width: 315px; height: 318px;
    background: linear-gradient(120deg, #dfe4ee 0%, #b7a7c6 30%, #6c5a9c 55%, #3c3f7a 80%, #1e2a55 100%);
  }
  .hero-hand {
    position: absolute;
    left: 215px; top: 200px;
    width: 150px; height: 118px;
    background: linear-gradient(160deg, #e6dede 0%, #c9a9a8 60%, #a97070 100%);
    border-radius: 40px 40px 0 0;
    opacity: 0.85;
  }
  .hero-title {
    position: absolute;
    left: 22px; top: 18px;
    font-size: 104px;
    font-weight: 800;
    line-height: 1;
    letter-spacing: 1px;
    color: var(--brand-blue);
  }
  .hero-sub {
    position: absolute;
    left: 26px; top: 132px;
    font-size: 18px;
    font-weight: 700;
    color: var(--brand-blue);
  }
  .hero-button {
    position: absolute;
    left: -40px; top: 168px;
    width: 255px; height: 72px;
    border-radius: 36px;
    background: var(--brand-navy);
    color: var(--white);
    font-size: 46px;
    font-weight: 800;
    letter-spacing: 2px;
    display: flex;
    align-items: center;
    padding-left: 66px;
    text-decoration: none;
  }

  /* Content sections */
  .services {
    display: flex;
    padding: 32px 20px 0 24px;
    gap: 28px;
    overflow: hidden;
  }
  .services-light { height: 386px; }
  .services-dark {
    height: 405px;
    background: linear-gradient(180deg, var(--band-blue), var(--band-deep));
    color: var(--white);
    padding-top: 36px;
  }
  .col-main { width: 430px; flex: none; }
  .col-side { width: 253px; flex: none; padding-top: 4px; }
  .section-heading {
    font-size: 24px;
    font-weight: 800;
    line-height: 1.2;
    color: var(--brand-blue);
    margin-bottom: 10px;
  }
  .col-side .section-heading { font-size: 21px; white-space: nowrap; }
  .services-dark .section-heading { color: var(--white); }
  .copy {
    font-size: 13px;
    line-height: 1.5;
    margin-bottom: 22px;
  }
  .col-side .copy { font-size: 12.5px; line-height: 1.55; }
  .services-dark .copy { color: #eef3f8; }
  .heading-gap { margin-top: 12px; }

  /* Footer */
  .site-footer {
    position: absolute;
    left: 0; bottom: 0;
    width: 755px; height: 45px;
    background: var(--footer-bg);
    display: flex;
    align-items: center;
    justify-content: center;
  }
  .site-footer a {
    font-size: 9px;
    font-weight: 700;
    color: var(--white);
    text-decoration: none;
    padding: 0 11px;
    border-left: 1px solid #8a8d91;
    line-height: 10px;
  }
  .site-footer a:first-child { border-left: none; }
</style>
</head>
<body>
  <header class="site-header">
    <div class="brand"><span class="brand-dot"></span>BRIGHTVANTAGE</div>
    <nav class="main-nav">
      <a href="#">HOME</a>
      <a href="#">ABOUT</a>
      <a href="#">BIG DATA AND ANALYTICS</a>
      <a href="#">PERCEPTION AND INFLUENCE</a>
      <a href="#">CASE STUDIES</a>
      <a href="#">CONTACT</a>
    </nav>
  </header>

  <section class="hero">
    <div class="hero-visual" role="img" aria-label="Digital head made of glowing circuit patterns in violet and blue tones"></div>
    <div class="hero-hand" role="img" aria-label="Hand holding a small glowing data element"></div>
    <h1 class="hero-title">EXPERT</h1>
    <p class="hero-sub">AT DATA COLLECTION AND ANALYSIS</p>
    <a class="hero-button" href="#">MORE</a>
  </section>

  <section class="services services-light">
    <div class="col-main">
      <h2 class="section-heading">SERVICES OFFERED<br>BY OUR BIG DATA DIVISION</h2>
      <p class="copy">Lorem ipsum dolor sit amet, mei nihil temporibus an, reformidans ullamcorper ad vel, est iriure nusquam lobortis at. Duis tisque cu sea. Te ignota cotidieque sea. Eos ut modo aperiam porteat.</p>
      <h2 class="section-heading heading-gap">TRULY TARGETED MARKETING &trade;</h2>
      <p class="copy">Lorem ipsum dolor sit amet, mei nihil temporibus an, reformidans ullamcorper ad vel, est iriure nusquam lobortis at. Duis tisque cu sea. Te ignota cotidieque sea. Eos ut modo aperiam porteat.</p>
      <p class="copy">Lorem ipsum dolor sit amet, mei nihil temporibus an, reformidans ullamcorper ad vel, est iriure nusquam lobortis at. Duis tisque cu sea. Te ignota cotidieque sea. Eos ut modo aperiam porteat.</p>
    </div>
    <div class="col-side">
      <h2 class="section-heading">MARKETING EXPERT</h2>
      <p class="copy">Lorem ipsum dolor sit amet, mei nihil temporibus an, reformidans ullamcorper ad vel, est iriure nusquam lobortis at. Duis tisque cu sea. Te ignota cotidieque sea. Eos ut modo aperiam porteat.</p>
      <h2 class="section-heading">TRULY TARGETED</h2>
      <p class="copy">Lorem ipsum dolor sit amet, mei nihil temporibus an, reformidans ullamcorper ad vel, est iriure nusquam lobortis at. Duis tisque cu sea. Te ignota cotidieque sea. Eos ut modo aperiam porteat.</p>
    </div>
  </section>

  <section class="services services-dark">
    <div class="col-main">
      <h2 class="section-heading">SERVICES OFFERED<br>BY OUR BIG DATA DIVISION</h2>
      <p class="copy">Lorem ipsum dolor sit amet, mei nihil temporibus an, reformidans ullamcorper ad vel, est iriure nusquam lobortis at. Duis tisque cu sea. Te ignota cotidieque sea. Eos ut modo aperiam porteat.</p>
      <h2 class="section-heading heading-gap">TRULY TARGETED MARKETING &trade;</h2>
      <p class="copy">Lorem ipsum dolor sit amet, mei nihil temporibus an, reformidans ullamcorper ad vel, est iriure nusquam lobortis at. Duis tisque cu sea. Te ignota cotidieque sea. Eos ut modo aperiam porteat.</p>
      <p class="copy">Lorem ipsum dolor sit amet, mei nihil temporibus an, reformidans ullamcorper ad vel, est iriure nusquam lobortis at. Duis tisque cu sea. Te ignota cotidieque sea. Eos ut modo aperiam porteat.</p>
    </div>
    <div class="col-side">
      <h2 class="section-heading">MARKETING EXPERT</h2>
      <p class="copy">Lorem ipsum dolor sit amet, mei nihil temporibus an, reformidans ullamcorper ad vel, est iriure nusquam lobortis at. Duis tisque cu sea. Te ignota cotidieque sea. Eos ut modo aperiam porteat.</p>
      <h2 class="section-heading">TRULY TARGETED</h2>
      <p class="copy">Lorem ipsum dolor sit amet, mei nihil temporibus an, reformidans ullamcorper ad vel, est iriure nusquam lobortis at. Duis tisque cu sea. Te ignota cotidieque sea. Eos ut modo aperiam porteat.</p>
    </div>
  </section>

  <footer class="site-footer">
    <a href="#">HOME</a>
    <a href="#">ABOUT</a>
    <a href="#">BIG DATA AND ANALYTICS</a>
    <a href="#">PERCEPTION AND INFLUENCE</a>
    <a href="#">CASE STUDIES</a>
    <a href="#">CONTACT</a>
  </footer>
</body>
</html>
```